Box Design for Concrete Mixer Truck Parts

Overview:
KVGEARS, a trusted supplier of concrete mixer, heavy-duty truck, and batch plant parts, is seeking a creative and professional packaging design for boxes that will contain concrete mixer truck parts. The design should reflect our brand identity while ensuring practicality and visual appeal.

Design Requirements:

Branding: The box must prominently feature the KVGEARS logo (attached).
Part Number Area: Include a designated space where part number stickers can be applied.
Color Scheme: The design should incorporate red as a primary color and may include up to three colors in total.
Style: The box should have a slick, modern, and creative design that aligns with our industry and brand.
Functionality: The design should be visually appealing while maintaining a professional and industrial feel, suitable for heavy-duty truck parts packaging.

We've included the box template and an example of a box using this template to help with orientation.

```html
<!DOCTYPE html>
<html lang="en">
<head>
<meta charset="utf-8">
<title>KVGEARS Parts Box Dieline</title>
<link href="https://fonts.googleapis.com/css2?family=Saira+Condensed:wght@500;700&display=swap" rel="stylesheet">
<style>
  :root {
    --brand-red: #ee0020;
    --brand-dark: #38453f;
    --paper: #ffffff;
    --cut-line: #2a2a2a;
    --fold-line: #444444;
    --mark-faint: rgba(255, 255, 255, 0.35);
  }
  html, body {
    margin: 0;
    padding: 0;
    overflow: hidden;
    background: var(--paper);
  }
  .canvas {
    width: 1200px;
    height: 1000px;
    display: block;
  }
  .panel-red { fill: var(--brand-red); }
  .panel-white { fill: var(--paper); }
  .band-dark { fill: var(--brand-dark); }
  .cut { fill: none; stroke: var(--cut-line); stroke-width: 1.4; }
  .fold { fill: none; stroke: var(--fold-line); stroke-width: 1.4; stroke-dasharray: 14 10; }
  .brand-name {
    font-family: "Saira Condensed", sans-serif;
    font-weight: 700;
    font-size: 40px;
    fill: var(--brand-dark);
    letter-spacing: 1px;
  }
  .brand-sub {
    font-family: "Saira Condensed", sans-serif;
    font-weight: 500;
    font-size: 17px;
    fill: var(--brand-dark);
  }
  .brand-square { fill: none; stroke: var(--brand-red); stroke-width: 4; }
  .tagline-small {
    font-family: "Saira Condensed", sans-serif;
    font-weight: 700;
    font-size: 24px;
    fill: var(--paper);
  }
  .tagline-large {
    font-family: "Saira Condensed", sans-serif;
    font-weight: 700;
    font-size: 46px;
    fill: var(--paper);
  }
  .mark-frame { fill: none; stroke: var(--mark-faint); stroke-width: 2; }
  .swatch-white { fill: var(--paper); stroke: var(--brand-dark); stroke-width: 1; }
</style>
</head>
<body>
<svg class="canvas" viewBox="150 290 1800 1500" xmlns="http://www.w3.org/2000/svg" role="img" aria-label="KVGEARS parts box dieline, flat">
  <defs>
    <g id="brand-lockup">
      <rect class="brand-square" x="2" y="-32" width="38" height="38"/>
      <text class="brand-name" x="48" y="0">KVGEARS</text>
      <text class="brand-sub" x="48" y="22">MIXER &amp; TRUCK GEARS CO, LLC</text>
    </g>
  </defs>

  <!-- Top tuck flap and lid -->
  <g class="lid">
    <path class="panel-red" d="M320 555 V505 Q320 432 395 432 H683 Q757 432 757 505 V555 Z"/>
    <path class="cut" d="M332 560 V515 Q332 444 400 444 H678 Q745 444 745 515 V560"/>
    <rect class="panel-red" x="313" y="548" width="450" height="218"/>
    <rect class="band-dark" x="313" y="768" width="450" height="29"/>
    <rect class="panel-white" x="325" y="797" width="427" height="116"/>
    <path class="fold" d="M382 567 H695"/>
    <g transform="rotate(180 538 700)">
      <text class="tagline-large" x="380" y="725" text-anchor="start">TRUCK PARTS</text>
      <text class="tagline-large" x="380" y="768">CONCRETE MIXER</text>
      <rect class="mark-frame" x="625" y="712" width="112" height="112"/>
      <use href="#brand-lockup" x="380" y="570"/>
    </g>
  </g>

  <!-- Dust flaps -->
  <path class="cut" d="M752 913 L770 890 L775 720 H1053 L1090 870 L1102 875 V918"/>
  <path class="cut" d="M1540 918 V875 L1550 868 L1588 720 H1866 L1870 895 L1888 918"/>

  <!-- Main wrap: glue flap + four walls -->
  <g class="walls">
    <path class="panel-white" d="M200 940 L325 913 H1888 L1900 930 V1300 H200 Z"/>
    <rect class="band-dark" x="200" y="1030" width="1700" height="30"/>
    <path class="panel-red" d="M200 1064 H1900 V1310 L1888 1300 H200 Z"/>
    <path class="cut" d="M325 913 L212 940 V1280 L325 1300"/>
    <path class="fold" d="M325 913 H752 M752 918 H1107 M1533 918 H1888 M325 1300 H1888"/>
    <path class="fold" d="M325 913 V1300 M752 913 V1300 M1107 918 V1300 M1533 918 V1300"/>

    <use href="#brand-lockup" x="382" y="1005"/>
    <use href="#brand-lockup" x="808" y="1005"/>
    <use href="#brand-lockup" x="1164" y="1005"/>
    <use href="#brand-lockup" x="1590" y="1005"/>

    <text class="tagline-small" x="808" y="1101">CONCRETE MIXER TRUCK PARTS</text>
    <text class="tagline-small" x="1590" y="1101">CONCRETE MIXER TRUCK PARTS</text>

    <text class="tagline-large" x="612" y="1204" text-anchor="end">CONCRETE MIXER</text>
    <text class="tagline-large" x="612" y="1247" text-anchor="end">TRUCK PARTS</text>
    <rect class="mark-frame" x="627" y="1176" width="112" height="112"/>

    <text class="tagline-large" x="1394" y="1204" text-anchor="end">CONCRETE MIXER</text>
    <text class="tagline-large" x="1394" y="1247" text-anchor="end">TRUCK PARTS</text>
    <rect class="mark-frame" x="1409" y="1176" width="112" height="112"/>
  </g>

  <!-- Bottom closure flaps -->
  <g class="bottom">
    <path class="panel-red" d="M320 1300 H757 V1605 H680 Q633 1605 633 1560 V1475 H445 V1560 Q445 1605 400 1605 H320 Z"/>
    <path class="cut" d="M332 1300 V1592 H405 Q432 1592 432 1560 V1475 M645 1475 V1560 Q645 1592 672 1592 H745 V1300"/>

    <path class="panel-red" d="M757 1300 V1315 L922 1408 Q934 1418 922 1432 Q888 1470 890 1480 Q895 1510 935 1510 H1113 V1300 Z"/>
    <path class="cut" d="M760 1318 L928 1410 Q936 1420 926 1432 Q900 1462 902 1475 Q906 1498 935 1498 H1100 V1300"/>

    <path class="panel-red" d="M1110 1300 L1210 1475 V1565 Q1210 1605 1255 1605 H1390 Q1433 1605 1433 1565 V1475 L1530 1300 Z"/>
    <path class="cut" d="M1113 1310 L1220 1478 V1562 Q1220 1592 1255 1592 H1390 Q1422 1592 1422 1562 V1478 L1527 1310"/>

    <path class="panel-red" d="M1528 1300 V1510 H1710 Q1750 1510 1754 1480 Q1756 1468 1722 1432 Q1710 1418 1722 1408 L1900 1312 V1300 Z"/>
    <path class="cut" d="M1540 1300 V1498 H1710 Q1740 1498 1742 1475 Q1744 1462 1716 1432 Q1706 1420 1714 1410 L1888 1314"/>
  </g>

  <!-- Colour swatch strip -->
  <g class="palette">
    <rect class="swatch-white" x="1536" y="1570" width="114" height="12"/>
    <rect class="panel-red" x="1650" y="1570" width="114" height="12"/>
    <rect class="band-dark" x="1764" y="1570" width="114" height="12"/>
  </g>
</svg>
</body>
</html>
```